Create Lanternfield HR Business Cards.

Create Business Cards for Lanternfield HR. 2 sided and Would like the back to have the logo.

Info for Business Card:
Address: 4827 Millbrook Ave Suite 230 Cleveland, Ohio 44987
Office Number: 216-555-0143
Mobile: 216-555-0192

Website: www.lanternfieldhr.example

Target Market(s)

Small to medium size businesses

Industry/Entity Type

Human Resources

Contact Information for Business Card

Company logo and information

Font styles to use
Serif
Sans Serif

Requirements
Must have
• Info for Business Card: Address: 4827 Millbrook Ave Suite 230 Cleveland, Ohio 44987 Office Number: 216-555-0143 Mobile: 216-555-0192 Website: www.lanternfieldhr.example

```html
<!DOCTYPE html>
<html lang="en">
<head>
<meta charset="utf-8">
<title>Lanternfield HR Business Cards</title>
<link href="https://fonts.googleapis.com/css2?family=Montserrat:wght@400;500;700;800&display=swap" rel="stylesheet">
<style>
  :root {
    --navy: #27215c;
    --navy-soft: #4f4a85;
    --orange: #e58428;
    --card: #fbfbfb;
    --card-back: #f0f0f0;
    --ink-grey: #555555;
    --page: #d9d9d9;
  }
  * { margin: 0; padding: 0; box-sizing: border-box; }
  html, body { width: 1200px; height: 1200px; overflow: hidden; }
  body {
    background: var(--page);
    font-family: "Montserrat", Arial, sans-serif;
    position: relative;
  }
  .card {
    position: absolute;
    left: 250px;
    width: 700px;
    height: 400px;
    border-radius: 22px;
    box-shadow: 0 6px 18px rgba(0,0,0,0.18);
    overflow: hidden;
  }
  .card-front { top: 150px; background: var(--card); }
  .card-back { top: 630px; background: var(--card-back); }

  .brand {
    display: flex;
    align-items: center;
    gap: 14px;
    color: var(--navy);
    font-weight: 800;
    letter-spacing: 0.5px;
    white-space: nowrap;
  }
  .brand-dot {
    border-radius: 50%;
    background: var(--orange);
    flex: none;
  }
  .card-front .brand {
    position: absolute;
    left: 50%; top: 50%;
    transform: translate(-50%, -50%);
    font-size: 46px;
  }
  .card-front .brand-dot { width: 44px; height: 44px; }

  .card-back .brand {
    position: absolute;
    right: 44px; top: 60px;
    font-size: 30px;
  }
  .card-back .brand-dot { width: 30px; height: 30px; }

  .person { position: absolute; left: 58px; top: 62px; }
  .person-name { font-size: 32px; font-weight: 700; color: var(--navy-soft); }
  .person-role { font-size: 18px; color: var(--ink-grey); margin: 4px 0 0 8px; }

  .contacts { position: absolute; left: 82px; top: 178px; list-style: none; }
  .contacts li {
    display: flex; align-items: center; gap: 10px;
    font-size: 18px; color: var(--ink-grey); line-height: 27px;
  }
  .contacts svg { width: 15px; height: 15px; fill: var(--navy-soft); flex: none; }

  .address-band {
    position: absolute;
    left: 130px; right: 36px; bottom: 40px;
    height: 62px;
    background: linear-gradient(90deg, var(--navy-soft), var(--navy));
    border-top: 3px solid var(--orange);
    border-radius: 0 0 18px 18px;
    display: flex; align-items: center;
    padding-left: 30px;
    color: #ffffff;
    font-size: 18px;
    letter-spacing: 0.3px;
  }
</style>
</head>
<body>

<section class="card card-front">
  <div class="brand"><span class="brand-dot"></span>Lanternfield HR</div>
</section>

<section class="card card-back">
  <div class="person">
    <h1 class="person-name">Dorian Wells</h1>
    <p class="person-role">Founder</p>
  </div>

  <ul class="contacts">
    <li><svg viewBox="0 0 24 24"><path d="M6.6 10.8a15 15 0 0 0 6.6 6.6l2.2-2.2c.3-.3.7-.4 1-.2 1.1.4 2.3.6 3.6.6.6 0 1 .4 1 1V20c0 .6-.4 1-1 1A17 17 0 0 1 3 4c0-.6.4-1 1-1h3.5c.6 0 1 .4 1 1 0 1.3.2 2.5.6 3.6.1.3 0 .7-.2 1z"/></svg>216-555-0143</li>
    <li><svg viewBox="0 0 24 24"><path d="M7 1h10a2 2 0 0 1 2 2v18a2 2 0 0 1-2 2H7a2 2 0 0 1-2-2V3a2 2 0 0 1 2-2zm0 3v14h10V4zm5 15.5a1 1 0 1 0 0 2 1 1 0 0 0 0-2z"/></svg>216-555-0192</li>
    <li><svg viewBox="0 0 24 24"><path d="M2 5h20v14H2zm2 2v.5l8 5 8-5V7z"/></svg>info@LanternfieldHR.example</li>
    <li><svg viewBox="0 0 24 24"><path d="M12 2a10 10 0 1 0 0 20 10 10 0 0 0 0-20zm6.9 9h-3a15 15 0 0 0-1.3-5.6A8 8 0 0 1 18.9 11zM12 4c.9 1.2 1.8 3.6 1.9 7h-3.8c.1-3.4 1-5.8 1.9-7zM9.4 5.4A15 15 0 0 0 8.1 11h-3a8 8 0 0 1 4.3-5.6zM5.1 13h3a15 15 0 0 0 1.3 5.6A8 8 0 0 1 5.1 13zM12 20c-.9-1.2-1.8-3.6-1.9-7h3.8c-.1 3.4-1 5.8-1.9 7zm2.6-1.4a15 15 0 0 0 1.3-5.6h3a8 8 0 0 1-4.3 5.6z"/></svg>www.lanternfieldhr.example</li>
  </ul>

  <div class="brand"><span class="brand-dot"></span>Lanternfield HR</div>

  <p class="address-band">4827 Millbrook Ave Suite 230 Cleveland, Ohio 44987</p>
</section>

</body>
</html>
```